Kestrel leadership hierchy redesign

Hi there, you created an awesome graphic design a while back. In our martial arts organization, elements are used to indicate an individuals leadership level and authority.
You start with a white uniform (black kestrel logos) and earn three different collars like a rising sun....
Purple, then Orange, Then Yellow.
After a student earns yellow collar....they will earn elemental logos on their black belt. We use to do colored collars for the wind, water, fire, and earth leadership levels but now we want to simplfy everything and put a colored hexagonal element logo in their black belt.
So after an individual earns a yellow collar.....
Their next goal is to either become a Program Director (Water) or a Lead Instructor (Wind)
For the Water Element, there are 4 levels you could earn as a logo on your black belt
Level 1 would be a Royal Blue hexagon outlined in white with our water symbol in the middle in white. Also label it with the rules to earn it: 50 Active Students
Level 2 would be a Royal Blue hexagon outlined in black with our water symbol in the middle in black.
Also label it with the rules to earn it: 100 Active Students
Level 3 would be a Royal Blue hexagon outlined in silver with our water symbol in the middle in silver.
Also label it with the rules to earn it: 150 Active Students.
Level 4 would be a Royal Blue hexagon outlined in silver with our water symbol in the middle in silver.
Also label it with the rules to earn it: 200
Active Students.
Chief Instructor Leadership Level (Fire) will follow the same guidelines as 4 level concept as water. Just change out water for fire and change out
Blue for red.
For Lead Instructor Wind , its only 1 level
Should be a white hexagon with a black outline and black wind symbol.
Final one, earth should be on top because its the hardest to obtain leadership wise. Same 4 levels as water and fire but the leadership requirements are diffrent.
Level 1 for earth
200 Active Students and 3 Active instructors who've earned elements.
Level 2 for earth
350 Active Students and 6 Active instructors who've earned elements.
Level 3 for earth
500 Active Students and 9 Active instructors who've earned elements.
Level 4 for earth
1000 Active Students and 18 Active instructors who've earned elements.
Label the graphic design with
Ignite Kestrel Path (on the bottom)
Serve Beyond Yourself (at the top)
Also i uploaded my belt posters so you dan gry to match the black/white/gold aethstetic. But please do elemental colored boxes like you did before in your previous design

```html
<!DOCTYPE html>
<html lang="en">
<head>
<meta charset="utf-8">
<title>Serve Beyond Yourself – Ignite Kestrel Path</title>
<link rel="stylesheet" href="https://fonts.googleapis.com/css2?family=Exo+2:wght@400;500;600;700;800;900&family=Krona+One&display=swap">
<style>
:root{
  --bg:#050505;
  --gold:#d6aa3c;
  --gold-light:#f3d27a;
  --gold-dark:#9c7420;
  --white:#f4f4f4;
  --silver:#c9c9cf;
  --black:#0a0a0a;
  --royal-blue:#2747c9;
  --blue-deep:#141a5e;
  --blue-mid:#2a3296;
  --earth-green:#2e8b3a;
  --green-deep:#0f2416;
  --green-mid:#2c4a30;
  --fire-red:#c8262a;
  --red-deep:#3a0709;
  --red-mid:#7c1b1e;
  --teal-deep:#0a2426;
  --teal-mid:#1a4c4c;
  --purple:#8b6bd0;
  --orange:#f06a22;
  --yellow:#f4e020;
  --head-font:"Exo 2",sans-serif;
  --title-font:"Krona One",sans-serif;
}
*{box-sizing:border-box;margin:0;padding:0}
html,body{width:740px;height:1200px;overflow:hidden;background:var(--bg)}
body{position:relative;font-family:var(--head-font);color:var(--white)}
.abs{position:absolute}

/* brand */
.brand{left:40px;top:25px;width:215px;height:215px;display:flex;flex-direction:column;align-items:center;justify-content:center;gap:10px}
.brand-dot{width:70px;height:70px;border-radius:50%;border:3px solid var(--gold)}
.brand-name{font-weight:700;font-size:26px;color:var(--gold);letter-spacing:2px;text-transform:uppercase}

/* title */
.title-rule{left:266px;top:50px;width:364px;height:3px;background:var(--gold)}
.title{left:264px;top:60px;font-family:var(--title-font);font-weight:400;line-height:52px;font-size:42px;letter-spacing:-1px;text-transform:uppercase;
  background:linear-gradient(180deg,var(--gold-light),var(--gold) 50%,var(--gold-dark));-webkit-background-clip:text;background-clip:text;color:transparent}
.title span{display:block}

/* panels */
.panel{border:3px solid var(--gold);overflow:hidden}
.panel-head{position:absolute;left:0;right:0;top:0;border-bottom:2px solid var(--gold);text-align:center}
.panel-title{font-weight:600;font-size:21px;letter-spacing:.5px;line-height:1}
.panel-sub{font-weight:800;font-size:11px;text-transform:uppercase;margin-top:6px}
.head-rule{width:190px;height:1px;margin:4px auto 0;background:rgba(255,255,255,.35)}
.shield-box{position:absolute;left:0;top:0;bottom:0;width:44px;background:#1b1b1b;display:flex;align-items:center;justify-content:center}
.sword{position:absolute;right:8px;top:8px}

.director{left:16px;top:254px;width:344px;height:398px;background:radial-gradient(ellipse at 70% 30%,var(--blue-mid),var(--blue-deep) 60%,#0b0e38)}
.director .panel-head{height:60px;background:linear-gradient(90deg,#0d1040,#141850);padding-top:10px}
.guardian{left:382px;top:254px;width:345px;height:761px;background:linear-gradient(180deg,var(--green-mid),var(--green-deep) 50%,var(--red-deep) 55%,var(--red-mid) 85%,var(--red-deep))}
.guardian .panel-head{height:60px;background:linear-gradient(90deg,#0c1a10,#17301c);padding-top:9px;padding-left:40px}
.chief-head{position:absolute;left:0;right:0;top:408px;height:56px;border-top:2px solid var(--gold);border-bottom:2px solid var(--gold);background:linear-gradient(90deg,#5a0d10,#3a080a);text-align:center;padding-top:8px}

.lead{left:382px;top:1030px;width:345px;height:133px;background:radial-gradient(ellipse at 60% 80%,var(--teal-mid),var(--teal-deep))}
.lead .panel-head{height:60px;background:linear-gradient(90deg,#0d2c2d,#163c3c);padding-top:9px}

/* hexagonal element badges */
.badge{position:absolute;width:52px;height:52px}
.badge polygon{stroke-width:3.5;stroke-linejoin:round}

/* levels */
.level{position:absolute;text-transform:uppercase}
.level-name{font-weight:600;font-size:16px;letter-spacing:1px;padding-bottom:2px;border-bottom:1px solid var(--line);width:170px}
.level-req{font-size:12px;font-weight:500;white-space:nowrap;padding-bottom:1px;border-bottom:1px solid var(--line)}
.level-req b{font-weight:800;font-size:21px;margin-right:4px;letter-spacing:.5px}
.gold-text{color:var(--gold)}
.director .level{--line:rgba(120,130,210,.6)}
.guardian .level{--line:rgba(80,140,80,.6)}
.guardian .level.fire{--line:rgba(200,80,80,.6)}
.earth .level-req b{font-size:19px}
.note{position:absolute;font-size:10.5px;line-height:12.5px}
.note em{font-style:normal;color:var(--gold)}

/* rising */
.rising{left:16px;top:668px;width:344px;height:229px;background:linear-gradient(180deg,#22222c,#0c0c12)}
.rising .panel-head{height:52px;padding-top:6px;background:#15151d}
.gi{position:absolute;top:80px;width:97px;height:100px;border-radius:8px;background:linear-gradient(180deg,#fafafa,#b9b9b9)}
.hours{position:absolute;top:180px;width:82px;height:46px;border-radius:0 0 8px 8px;background:#16161c;text-align:center;line-height:1}
.hours b{display:block;font-size:21px;font-weight:800;margin-top:5px}
.hours span{font-size:14px;font-weight:500}

.goal{position:absolute;top:921px;width:142px;height:61px;border:3px solid var(--gold);background:linear-gradient(135deg,var(--teal-mid),var(--teal-deep));text-align:center;text-transform:uppercase;line-height:1}
.goal .g1{font-size:10.5px;font-weight:600;margin-top:3px;padding-bottom:2px;border-bottom:1px solid rgba(255,255,255,.4)}
.goal .g2{font-size:10.5px;font-weight:600;padding:2px 0;border-bottom:1px solid rgba(255,255,255,.4)}
.goal .g3{font-size:24px;font-weight:800;margin-top:2px;text-transform:none}
.goal .g3 span{font-size:17px;font-weight:600}

/* age */
.age{left:16px;top:998px;width:344px;height:100px;background:linear-gradient(180deg,#1c1c24,#0e0e14)}
.age .panel-head{height:26px;padding-top:3px;background:#17171f}
.age .panel-title{font-size:16px}
.age-row{position:absolute;font-size:9.5px;line-height:11px;display:flex;align-items:center}
.tag{display:inline-block;width:72px;text-align:right;padding-right:3px;color:var(--white)}
.arrow{margin:0 6px;width:20px;height:1px;background:var(--white);position:relative}
.arrow::after{content:"";position:absolute;right:-1px;top:-2px;border-left:4px solid var(--white);border-top:2.5px solid transparent;border-bottom:2.5px solid transparent}

.footer{left:28px;top:1114px;font-family:var(--title-font);font-weight:400;font-size:27px;line-height:34px;letter-spacing:-1px;text-transform:uppercase;
  background:linear-gradient(180deg,var(--gold-light),var(--gold) 55%,var(--gold-dark));-webkit-background-clip:text;background-clip:text;color:transparent}
</style>
</head>
<body>

<div class="abs brand">
  <div class="brand-dot"></div>
  <div class="brand-name">Kestrel</div>
</div>
<div class="abs title-rule"></div>
<h1 class="abs title"><span>Serve</span><span>Beyond</span><span>Yourself</span></h1>

<!-- Program Director (Water) -->
<section class="abs panel director">
  <div class="panel-head">
    <div class="shield-box"><svg width="30" height="36" viewBox="0 0 30 36"><path d="M15 2 L27 7 V17 C27 26 21 31 15 34 C9 31 3 26 3 17 V7 Z" fill="none" stroke="#e8e8e8" stroke-width="3"/><path d="M15 5 L25 9 V17 C25 24 20 29 15 31 Z" fill="#e8e8e8"/></svg></div>
    <div class="panel-title">Program Director</div>
    <div class="head-rule"></div>
    <div class="panel-sub">Support</div>
  </div>
  <svg class="badge" style="left:29px;top:71px" viewBox="0 0 52 52" role="img" aria-label="Water element, level 4: royal blue hexagon with silver outline and silver water symbol"><polygon points="26,3 46,14.5 46,37.5 26,49 6,37.5 6,14.5" fill="var(--royal-blue)" stroke="var(--silver)"/></svg>
  <div class="level" style="left:90px;top:72px"><div class="level-name gold-text">Level 4</div><div class="level-req gold-text"><b>200</b>Active Students</div></div>
  <svg class="badge" style="left:29px;top:142px" viewBox="0 0 52 52" role="img" aria-label="Water element, level 3: royal blue hexagon with silver outline and silver water symbol"><polygon points="26,3 46,14.5 46,37.5 26,49 6,37.5 6,14.5" fill="var(--royal-blue)" stroke="var(--silver)"/></svg>
  <div class="level" style="left:90px;top:143px"><div class="level-name">Level 3</div><div class="level-req"><b>150</b>Active Students</div></div>
  <svg class="badge" style="left:29px;top:211px" viewBox="0 0 52 52" role="img" aria-label="Water element, level 2: royal blue hexagon with black outline and black water symbol"><polygon points="26,3 46,14.5 46,37.5 26,49 6,37.5 6,14.5" fill="var(--royal-blue)" stroke="var(--black)"/></svg>
  <div class="level" style="left:90px;top:212px"><div class="level-name">Level 2</div><div class="level-req"><b>100</b>Active Students</div></div>
  <svg class="badge" style="left:29px;top:281px" viewBox="0 0 52 52" role="img" aria-label="Water element, level 1: royal blue hexagon with white outline and white water symbol"><polygon points="26,3 46,14.5 46,37.5 26,49 6,37.5 6,14.5" fill="var(--royal-blue)" stroke="var(--white)"/></svg>
  <div class="level" style="left:90px;top:282px"><div class="level-name">Level 1</div><div class="level-req"><b>50</b>Active Students</div></div>
  <p class="note" style="left:24px;top:350px;width:290px"><em>Note:</em> Only 1 Program Director per school may be acknowledged with a Level 2, 3, or 4. This partner is chosen from the head instructor of a school.</p>
</section>

<!-- Guardian (Earth) & Chief (Fire) -->
<section class="abs panel guardian">
  <div class="panel-head">
    <div class="shield-box"><svg width="30" height="36" viewBox="0 0 30 36"><path d="M15 2 L27 7 V17 C27 26 21 31 15 34 C9 31 3 26 3 17 V7 Z" fill="none" stroke="#e8e8e8" stroke-width="3"/><path d="M15 5 L25 9 V17 C25 24 20 29 15 31 Z" fill="#e8e8e8"/></svg></div>
    <div class="panel-title">Guardian Instructor</div>
    <div class="head-rule"></div>
    <div class="panel-sub" style="font-size:9.5px;margin-top:5px">Main charge to a family of kestrel instructors</div>
    <svg class="sword" width="14" height="44" viewBox="0 0 14 44"><rect x="6" y="2" width="2" height="40" fill="#ddd"/><rect x="1" y="10" width="12" height="2" fill="#ddd"/></svg>
  </div>

  <div class="earth">
    <svg class="badge" style="left:30px;top:78px" viewBox="0 0 52 52" role="img" aria-label="Earth element, level 4: green hexagon with silver outline and silver earth symbol"><polygon points="26,3 46,14.5 46,37.5 26,49 6,37.5 6,14.5" fill="var(--earth-green)" stroke="var(--silver)"/></svg>
    <div class="level" style="left:92px;top:70px"><div class="level-name gold-text">Level 4</div><div class="level-req gold-text"><b>1000</b>Active Students</div><div class="level-req gold-text"><b>18</b>Active Legacy Instructors</div></div>
    <svg class="badge" style="left:30px;top:162px" viewBox="0 0 52 52" role="img" aria-label="Earth element, level 3: green hexagon with silver outline and silver earth symbol"><polygon points="26,3 46,14.5 46,37.5 26,49 6,37.5 6,14.5" fill="var(--earth-green)" stroke="var(--silver)"/></svg>
    <div class="level" style="left:92px;top:154px"><div class="level-name">Level 3</div><div class="level-req"><b>500</b>Active Students</div><div class="level-req"><b>9</b>Active Legacy Instructors</div></div>
    <svg class="badge" style="left:30px;top:246px" viewBox="0 0 52 52" role="img" aria-label="Earth element, level 2: green hexagon with black outline and black earth symbol"><polygon points="26,3 46,14.5 46,37.5 26,49 6,37.5 6,14.5" fill="var(--earth-green)" stroke="var(--black)"/></svg>
    <div class="level" style="left:92px;top:238px"><div class="level-name">Level 2</div><div class="level-req"><b>350</b>Active Students</div><div class="level-req"><b>6</b>Active Legacy Instructors</div></div>
    <svg class="badge" style="left:30px;top:330px" viewBox="0 0 52 52" role="img" aria-label="Earth element, level 1: green hexagon with white outline and white earth symbol"><polygon points="26,3 46,14.5 46,37.5 26,49 6,37.5 6,14.5" fill="var(--earth-green)" stroke="var(--white)"/></svg>
    <div class="level" style="left:92px;top:322px"><div class="level-name">Level 1</div><div class="level-req"><b>200</b>Active Students</div><div class="level-req"><b>3</b>Active Legacy Instructors</div></div>
  </div>

  <div class="chief-head">
    <div class="panel-title">Chief Instructor</div>
    <div class="head-rule" style="width:290px"></div>
    <div class="panel-sub" style="font-size:11.5px;margin-top:4px">Main charge to a family of students</div>
    <svg class="sword" width="14" height="44" viewBox="0 0 14 44"><rect x="6" y="2" width="2" height="40" fill="#ddd"/><rect x="1" y="10" width="12" height="2" fill="#ddd"/></svg>
  </div>
  <svg class="badge" style="left:30px;top:483px" viewBox="0 0 52 52" role="img" aria-label="Fire element, level 4: red hexagon with silver outline and silver fire symbol"><polygon points="26,3 46,14.5 46,37.5 26,49 6,37.5 6,14.5" fill="var(--fire-red)" stroke="var(--silver)"/></svg>
  <div class="level fire" style="left:97px;top:484px"><div class="level-name gold-text">Level 4</div><div class="level-req gold-text"><b>200</b>Active Students</div></div>
  <svg class="badge" style="left:30px;top:550px" viewBox="0 0 52 52" role="img" aria-label="Fire element, level 3: red hexagon with silver outline and silver fire symbol"><polygon points="26,3 46,14.5 46,37.5 26,49 6,37.5 6,14.5" fill="var(--fire-red)" stroke="var(--silver)"/></svg>
  <div class="level fire" style="left:97px;top:551px"><div class="level-name">Level 3</div><div class="level-req"><b>150</b>Active Students</div></div>
  <svg class="badge" style="left:30px;top:619px" viewBox="0 0 52 52" role="img" aria-label="Fire element, level 2: red hexagon with black outline and black fire symbol"><polygon points="26,3 46,14.5 46,37.5 26,49 6,37.5 6,14.5" fill="var(--fire-red)" stroke="var(--black)"/></svg>
  <div class="level fire" style="left:97px;top:620px"><div class="level-name">Level 2</div><div class="level-req"><b>100</b>Active Students</div></div>
  <svg class="badge" style="left:30px;top:689px" viewBox="0 0 52 52" role="img" aria-label="Fire element, level 1: red hexagon with white outline and white fire symbol"><polygon points="26,3 46,14.5 46,37.5 26,49 6,37.5 6,14.5" fill="var(--fire-red)" stroke="var(--white)"/></svg>
  <div class="level fire" style="left:97px;top:690px"><div class="level-name">Level 1</div><div class="level-req"><b>50</b>Active Students</div></div>
</section>

<!-- Rising -->
<section class="abs panel rising">
  <div class="panel-head">
    <div class="panel-title">Rising Kestrel Instructors</div>
    <div class="head-rule" style="width:250px"></div>
    <div class="panel-sub" style="font-size:16px;margin-top:1px">New Day</div>
  </div>
  <div class="gi" style="left:10px" role="img" aria-label="White uniform with purple collar and black belt"></div>
  <div class="hours" style="left:18px"><b>100</b><span>Hours</span></div>
  <div class="gi" style="left:121px" role="img" aria-label="White uniform with orange collar and black belt"></div>
  <div class="hours" style="left:129px"><b>200</b><span>Hours</span></div>
  <div class="gi" style="left:232px" role="img" aria-label="White uniform with yellow collar and black belt"></div>
  <div class="hours" style="left:240px"><b>300</b><span>Hours</span></div>
</section>

<svg class="abs" style="left:0;top:0" width="740" height="1200" viewBox="0 0 740 1200" aria-hidden="true">
  <g stroke="#d6aa3c" stroke-width="3" fill="#d6aa3c">
    <line x1="262" y1="848" x2="193" y2="912"/>
    <polygon points="186,920 190,906 200,914" stroke-width="1"/>
    <line x1="338" y1="848" x2="338" y2="908"/>
    <polygon points="338,918 333,904 343,904" stroke-width="1"/>
  </g>
</svg>

<div class="goal" style="left:48px"><div class="g1">Level 1</div><div class="g2">Program Director</div><div class="g3">400 <span>Hours</span></div></div>
<div class="goal" style="left:208px"><div class="g1">Level 1</div><div class="g2">Lead Instructor</div><div class="g3">400 <span>Hours</span></div></div>

<!-- Age -->
<section class="abs panel age">
  <div class="panel-head"><div class="panel-title">Minimum Age Requirement</div></div>
  <div class="age-row" style="left:70px;top:33px"><span class="tag" style="background:var(--purple)">Purple Collar</span><span class="arrow"></span>Minimum Age 10 years old</div>
  <div class="age-row" style="left:70px;top:45px"><span class="tag" style="background:var(--orange)">Orange Collar</span><span class="arrow"></span>Minimum Age 13 years old</div>
  <div class="age-row" style="left:70px;top:57px"><span class="tag" style="background:var(--yellow);color:#333">Yellow Collar</span><span class="arrow"></span>Minimum Age 16 years old</div>
  <div class="age-row" style="left:6px;top:70px"><span style="width:136px;text-align:right">Level 1 Program Director<br>and Level 1 Lead Instructor</span><span class="arrow" style="margin:0 14px 0 26px"></span><span>Minimum Age 18 years old and<br>Minimum Rank of Black Belt</span></div>
</section>

<div class="abs footer">Ignite Kestrel<br>Path</div>

<!-- Lead (Wind) -->
<section class="abs panel lead">
  <div class="panel-head">
    <div class="shield-box" style="width:46px"><svg width="30" height="36" viewBox="0 0 30 36"><path d="M15 2 L27 7 V17 C27 26 21 31 15 34 C9 31 3 26 3 17 V7 Z" fill="none" stroke="#e8e8e8" stroke-width="3"/><path d="M15 5 L25 9 V17 C25 24 20 29 15 31 Z" fill="#e8e8e8"/></svg></div>
    <div class="panel-title" style="font-size:24px;padding-left:10px">Lead Instructor</div>
    <div class="head-rule" style="width:200px"></div>
    <div class="panel-sub" style="margin-top:4px">Support</div>
    <svg class="sword" width="14" height="44" viewBox="0 0 14 44"><rect x="6" y="2" width="2" height="40" fill="#ddd"/><rect x="1" y="10" width="12" height="2" fill="#ddd"/></svg>
  </div>
  <svg class="badge" style="left:30px;top:69px" viewBox="0 0 52 52" role="img" aria-label="Wind element, level 1: white hexagon with black outline and black wind symbol"><polygon points="26,3 46,14.5 46,37.5 26,49 6,37.5 6,14.5" fill="var(--white)" stroke="var(--black)"/></svg>
  <div class="level" style="left:105px;top:66px;--line:rgba(120,190,180,.5)"><div class="level-name" style="text-align:center;width:170px">Level 1</div></div>
  <p class="note" style="left:90px;top:92px;width:245px;font-size:7.2px;line-height:8.2px"><em>Note:</em> Individual may pursue teaching kestrel martial arts in their own club or school with both a Guardian Instructor and their head instructors approval.</p>
</section>

</body>
</html>
```